ZESTRO - Sydney Based Technology Consultancy -Logo & Business Card design

Who are we?
-
Zestro is an emerging and advanced technology consulting and professional services business based in Sydney, Australia. Zestro specialising in increasing value to organisations through the effective use of current and emerging technologies, ensuring that technology is a sustainable catalyst to attaining stated business goals.

We pride ourselves in challenging the norm.

What do we want?
-
We are looking to update our "Brand" we already have a simple “home grown” logo and we are now looking for a new one, once we have this updated logo and businesses look and feel though the business card design we will refresh our website with the new logo and design thus updating the Companies overall look at feel.

Our current site is www.zestro.net.au is a very basic wordpress site and we will be updating it once we have the new logo and designs done

Our initial thoughts on the new Zestro identity are
• Logo Concept
- One of the key things is obviously the 8
- I was thinking that a logo that had 8 as the core of the logo would be cool,
- Almost like having a “ring” or hoop that is twisted to form an 8 with different services scribed on the inside.
- So we would have a Large 8 and the inside would have ring each service or section engraved.

• Brand / web Feel
- Simple
- Professional
- Innovative
- Clear
- Destination
- Unique
- Impartial
- Safe
- Leading edge
- Familiar

- Emerging technologies
- White and ice / glacier blue
- The familiar feel of the Quillon web site
- Embedded specialist Video clips

• Portfolio of Services
- Zestro – A bright hub for bright minds
- Zestro – we supply the path to turn concepts from notion to outcome
- Focus should be on the brand quality consistent clear local knowledge with regional, national, theatre and global presence

Access to Specialists
- Emerging technologies
- Sustainability
- Collaboration
- Data centre
- Virtualisation

• Adjacent ideas under the one Brand
- Plexoro – Enable Business Collaboration
- Vantor – Infrastructure Virtualisation
- skolo - smart people and processes
- brevix - Emerging technologies
- maldoro - business to technology integration
- tessun - Smart Infrastructure
- wyn – Connected communities
- orba - sustainability

Target Market(s)

Australia, New Zealand and Asia pacific organisations that are typically English speaking.
Markets
- IT & Technology partners
- Banking and Finance
- Health

Industry/Entity Type

Business

Requirements
Must have
• Logo
Business cards
Colour pallette
3D Logo
Nice to have
• Style guide
Designer who can also assist with new Wordpress design
Should not have
• we don't want cheap looking, overtly flashy or gimmicky logo.

```html
<!DOCTYPE html>
<html lang="en">
<head>
<meta charset="utf-8">
<title>Zestro – Business Card</title>
<link rel="stylesheet" href="https://fonts.googleapis.com/css2?family=Open+Sans:ital,wght@0,400;0,600;0,700;1,300&display=swap">
<style>
  :root {
    --backdrop: #cfcfcf;
    --card-navy: #43567a;
    --band-navy: #3a4d7b;
    --ink-navy: #1f3a6e;
    --logo-steel: #5a6d8e;
    --paper: #f6f9fb;
    --bubble-line: #c9d6d2;
    --muted: #8a93a0;
    --photo-frame: #c9a640;
    --white: #ffffff;
  }
  * { box-sizing: border-box; margin: 0; padding: 0; }
  html, body {
    width: 1200px; height: 900px; overflow: hidden;
    background: var(--backdrop);
    font-family: "Open Sans", Arial, sans-serif;
  }
  .stage { position: relative; width: 1200px; height: 900px; }

  .card { position: absolute; box-shadow: 0 6px 18px rgba(0,0,0,.22); }

  /* Back of card */
  .card-back {
    left: 110px; top: 290px; width: 560px; height: 320px;
    background: var(--card-navy);
    display: flex; align-items: center; justify-content: center;
  }
  .card-back .brand-name {
    color: var(--white); font-weight: 700; font-size: 84px; letter-spacing: 1px;
  }

  /* Front of card */
  .card-front {
    left: 760px; top: 170px; width: 320px; height: 560px;
    background: var(--paper);
    display: flex; flex-direction: column;
  }
  .front-body { flex: 1; padding: 30px 26px 0 26px; }
  .front-logo {
    text-align: right; color: var(--logo-steel);
    font-weight: 700; font-size: 56px; line-height: 1;
  }
  .name-bubble {
    position: relative; margin-top: 34px;
    border: 1.5px solid var(--bubble-line); border-radius: 8px;
    background: var(--white);
    padding: 14px 16px; display: flex; align-items: center; gap: 10px;
  }
  .name-bubble svg.tail { position: absolute; left: 18px; top: -13px; }
  .portrait {
    width: 46px; height: 46px; flex: none;
    border: 2px solid var(--photo-frame);
    background: linear-gradient(135deg, #8a6d55, #c8b6a0);
  }
  .person-name { color: var(--ink-navy); font-weight: 700; font-size: 29px; line-height: 1.05; }
  .person-role { color: var(--muted); font-style: italic; font-weight: 300; font-size: 15px; }
  .contact {
    list-style: none; margin-top: 18px; padding-left: 4px;
    color: var(--ink-navy); font-weight: 700; font-size: 13px; line-height: 1.55;
  }
  .web-band {
    height: 64px; background: var(--band-navy);
    display: flex; align-items: center; justify-content: center;
    color: var(--white); font-weight: 600; font-size: 28px; letter-spacing: .5px;
  }
</style>
</head>
<body>
<main class="stage">
  <section class="card card-back" aria-label="Business card back">
    <span class="brand-name">Zestro</span>
  </section>

  <section class="card card-front" aria-label="Business card front">
    <div class="front-body">
      <div class="front-logo">Zestro</div>
      <div class="name-bubble">
        <svg class="tail" width="22" height="14" viewBox="0 0 22 14" aria-hidden="true">
          <path d="M1 14 L6 1 L21 14" fill="#ffffff" stroke="#c9d6d2" stroke-width="1.5"/>
        </svg>
        <div class="portrait" role="img" aria-label="Staff portrait photo"></div>
        <div>
          <div class="person-name">Your Name</div>
          <div class="person-role">Job description</div>
        </div>
      </div>
      <ul class="contact">
        <li>1234 Street Name, City, State, Zip</li>
        <li>you@zestro.com.au</li>
        <li>Phone Number</li>
      </ul>
    </div>
    <div class="web-band">zestro.com.au</div>
  </section>
</main>
</body>
</html>
```